QV - menu design

Hi,

We require elegant menu design for upscale restaurant. Please find attached the logo and the menu items for your reference.

for inspiration, this is a good website: -
http://www.platewhisper.example/bellfoldnotes/about.php

We are very much open for Menu Size suggestions.

unfortunately the place is going under renovation, we don't have updated images to it. the closest look and feel to our place is http://varnelo.example ..

we are also open for creative options on the shape, the styles, etc. as long as it represents the fine dine feel ...

Thanks ...

Dear All,

We wouldlike to extend our apology for not being able to provide feedbacks on everysingle design. We were extremely busy and we have multiple contests opensimultaneously which makes the process even harder.

However,we would like to thank you all for the efforts you have put into designingour menu. It is very much appreciated …

We wishyou all success in your design ventures and we are quite positive that we willbe working with many of you on many projects in the soon future. 

Thanks & Regards,

TLG Team...

 

 

 

Industry/Entity Type

Restaurant

Requirements
Must have
• Please ensure that there are 'some' images in the menu ... this is very important.
Should not have
• IMPORTANT: -

1. Please DO NOT insert any currency sign to the menu
2. Please keep the prices of the menu at the end of the menu items descriptions NOT beside the menu item names. The font of the price should be similar to the menu item description and please DO NOT bold the numbers. the prices should be subtle.

Thank you ...

```html
<!DOCTYPE html>
<html lang="en">
<head>
<meta charset="utf-8">
<title>Soup Menu</title>
<link rel="stylesheet" href="https://fonts.googleapis.com/css2?family=Ubuntu:wght@300;500;700&display=swap">
<style>
  :root {
    --paper: #f0efee;
    --taupe: #8a7661;
    --title: #7b6a59;
    --body: #8d8984;
    --rule: #a99b8b;
    --frame: #b09d84;
  }
  * { margin: 0; padding: 0; box-sizing: border-box; }
  html, body { width: 1200px; height: 2700px; overflow: hidden; background: var(--paper); }
  .menu-panel { position: relative; width: 1200px; height: 2700px; background: var(--paper); font-family: "Ubuntu", sans-serif; }
  .guides { position: absolute; inset: 0; }
  .section-badge {
    position: absolute; left: 82px; top: 170px; width: 360px; height: 360px;
    border-radius: 50%; background: var(--taupe);
    display: flex; align-items: center; justify-content: center;
  }
  .section-badge h1 { color: #fff; font-weight: 500; font-size: 58px; letter-spacing: 1px; }
  .dish { position: absolute; left: 90px; width: 1080px; }
  .dish h2 { color: var(--title); font-weight: 700; font-size: 50px; letter-spacing: 12px; line-height: 1; margin-bottom: 10px; white-space: nowrap; }
  .dish p { color: var(--body); font-weight: 300; font-size: 41px; line-height: 50px; white-space: nowrap; }
  .dish--bouillabaisse { top: 592px; }
  .dish--barley { top: 848px; }
  .dish--chili { top: 1094px; }
  .dish-photo { position: absolute; }
  .dish-photo--seafood { left: 318px; top: 1292px; }
  .dish-photo--barley { left: 72px; top: 1808px; }
  .dish-photo--chili { left: 716px; top: 1812px; }
</style>
</head>
<body>
<main class="menu-panel">
  <svg class="guides" width="1200" height="2700" viewBox="0 0 1200 2700" aria-hidden="true">
    <g stroke="var(--rule)" stroke-width="2" stroke-dasharray="12 9" fill="none">
      <line x1="268" y1="0" x2="268" y2="160"/>
      <line x1="278" y1="2236" x2="278" y2="2700"/>
      <line x1="602" y1="1876" x2="602" y2="2700"/>
      <line x1="926" y1="2240" x2="926" y2="2700"/>
    </g>
  </svg>

  <div class="section-badge"><h1>SOUP</h1></div>

  <section class="dish dish--bouillabaisse">
    <h2>Bouillabaisse</h2>
    <p>Traditional French Seafood soup, with Saffron and<br>Estragon. 119</p>
  </section>
  <section class="dish dish--barley">
    <h2>Barley soup</h2>
    <p>With fresh vegetables, tomato smoothie and a hint of<br>garlic oil. 49</p>
  </section>
  <section class="dish dish--chili">
    <h2>Beef chili</h2>
    <p>Served with Arabic bread, fresh guacamole and spicy<br>black beans. 49</p>
  </section>

  <svg class="dish-photo dish-photo--seafood" width="576" height="576" viewBox="0 0 576 576" role="img" aria-label="Photo of bouillabaisse with mussels, prawns and crab in a saffron tomato broth">
    <defs>
      <radialGradient id="seafood-tone" cx="50%" cy="45%" r="55%">
        <stop offset="0" stop-color="#b9462a"/>
        <stop offset="0.55" stop-color="#c8603a"/>
        <stop offset="0.85" stop-color="#d9d4c8"/>
        <stop offset="1" stop-color="#cfe0e0"/>
      </radialGradient>
    </defs>
    <circle cx="288" cy="288" r="285" fill="url(#seafood-tone)" stroke="var(--frame)" stroke-width="3"/>
  </svg>

  <svg class="dish-photo dish-photo--barley" width="416" height="416" viewBox="0 0 416 416" role="img" aria-label="Photo of barley soup with carrots, corn and tomato on a spoon">
    <defs>
      <radialGradient id="barley-tone" cx="50%" cy="55%" r="60%">
        <stop offset="0" stop-color="#d7b48c"/>
        <stop offset="0.6" stop-color="#d0743a"/>
        <stop offset="1" stop-color="#c7572a"/>
      </radialGradient>
    </defs>
    <circle cx="208" cy="208" r="205" fill="url(#barley-tone)" stroke="var(--frame)" stroke-width="3"/>
  </svg>

  <svg class="dish-photo dish-photo--chili" width="416" height="416" viewBox="0 0 416 416" role="img" aria-label="Photo of beef chili with kidney beans and a fork">
    <defs>
      <radialGradient id="chili-tone" cx="50%" cy="50%" r="60%">
        <stop offset="0" stop-color="#8a2e1c"/>
        <stop offset="0.7" stop-color="#6e2214"/>
        <stop offset="1" stop-color="#9a3a22"/>
      </radialGradient>
    </defs>
    <circle cx="208" cy="208" r="205" fill="url(#chili-tone)" stroke="var(--frame)" stroke-width="3"/>
  </svg>
</main>
</body>
</html>
```